Flyer for Beacon Ledger & Returns, a local tax practice

Flyer for my business to be distributed locally in the Western Suburb of Melbourne (Size: DL, Fold: Flat, Backside: Blank) This will include below information (Font, color and capitalization of the text is for the designer's creativity):
Beacon Ledger & Returns Your Local Tax Accountant
ABN: 71 284 519 036
Address: 9 Mirra Close, Tarwin Heights
dovpelk@blrau.com.au
Call Florin on 0417 865 209 to book your appointment
Services we offer:
Individual & Company Tax Returns
Company & Trust formation
Business Advisory
Bookkeeping
BAS & IAS
Payroll
TPAR
Please include the logo of the business attached which was designed by ArtHarbor few years ago.
Please include the QNE, WRD and Pulva logos somewhere in the bottom, preferable the same size and aligned (attached)

```html
<!DOCTYPE html>
<html lang="en">
<head>
<meta charset="utf-8">
<title>Beacon Ledger &amp; Returns — Flyer</title>
<link rel="stylesheet" href="https://fonts.googleapis.com/css2?family=Oswald:wght@500&family=Montserrat:wght@500;600;700;800&family=Fira+Sans:wght@500&family=Lato:wght@400&display=swap">
<style>
  :root{
    --orange:#f07a32;
    --orange-deep:#f15a2b;
    --orange-light:#f88a24;
    --ink:#454547;
    --text:#4a4a4c;
    --band:#48494b;
    --paper:#ffffff;
  }
  *{margin:0;padding:0;box-sizing:border-box}
  html,body{width:732px;height:1200px;overflow:hidden;background:var(--paper)}
  .flyer{position:relative;width:732px;height:1200px;background:var(--paper);font-family:"Montserrat",sans-serif}

  .header{position:absolute;left:0;top:0;width:732px;height:121px}
  .brand{position:absolute;left:44px;top:40px;display:flex;align-items:center;gap:12px}
  .brand-mark{width:40px;height:40px;background:var(--ink)}
  .brand-name{font-family:"Montserrat",sans-serif;font-weight:700;font-size:21px;color:var(--orange);line-height:1.05;width:190px}
  .booking{position:absolute;right:32px;top:48px;display:flex;align-items:center;gap:8px}
  .booking svg{width:36px;height:36px}
  .booking-label{font-size:8px;font-weight:600;color:var(--ink);letter-spacing:.2px;margin-left:4px}
  .booking-number{font-size:23px;font-weight:700;color:var(--orange);line-height:1.05}

  .hero{position:absolute;left:0;top:121px;width:732px;height:506px;
    background:linear-gradient(160deg,#d9dcd8 0%,#c9d6df 25%,#8fb2cf 45%,#b9a27c 60%,#d8cdb9 75%,#e9e6e1 100%)}
  .hero-banner{position:absolute;left:0;top:411px;width:569px;height:216px;
    background:linear-gradient(90deg,var(--orange-light) 0%,#f57a28 55%,var(--orange-deep) 100%);
    border-top-right-radius:56px;opacity:.97}
  .hero-title{position:absolute;left:48px;top:433px;font-family:"Oswald",sans-serif;font-weight:500;
    font-size:44px;line-height:48px;color:#fff;letter-spacing:.2px}

  .offer{position:absolute;left:35px;top:633px}
  .offer-lead{font-size:34px;font-weight:500;color:var(--ink);line-height:40px}
  .offer-title{font-size:64px;font-weight:800;color:var(--orange);line-height:66px;letter-spacing:-.5px}
  .offer-rule{position:absolute;left:35px;top:764px;width:204px;height:7px;background:var(--orange)}

  .service{position:absolute;display:flex;align-items:center;gap:10px;
    font-family:"Fira Sans",sans-serif;font-weight:500;font-size:26px;color:var(--text);white-space:nowrap}
  .service-icon{width:46px;height:46px;background:var(--orange);display:flex;align-items:center;justify-content:center;flex:none}
  .service-icon svg{width:28px;height:28px;fill:none;stroke:#fff;stroke-width:1.6;stroke-linecap:round;stroke-linejoin:round}

  .contact-band{position:absolute;left:0;top:1084px;width:732px;height:53px;background:var(--band);
    display:flex;align-items:center;font-family:"Lato",sans-serif;font-size:17px;color:#fff}
  .contact-item{position:absolute;display:flex;align-items:center;gap:10px}
  .contact-icon{width:22px;height:22px;background:var(--orange);border-radius:3px;display:flex;align-items:center;justify-content:center}
  .contact-icon svg{width:16px;height:16px;fill:none;stroke:#fff;stroke-width:1.5}

  .abn{position:absolute;left:0;top:1154px;width:732px;height:24px;display:flex;align-items:center;gap:12px;
    font-family:"Lato",sans-serif;font-size:16px;color:var(--text)}
  .abn-line{flex:1;height:1.5px;background:var(--orange)}
  .abn-label{color:var(--orange)}
</style>
</head>
<body>
<div class="flyer">

  <header class="header">
    <div class="brand">
      <span class="brand-mark"></span>
      <span class="brand-name">Beacon Ledger &amp; Returns</span>
    </div>
    <div class="booking">
      <svg viewBox="0 0 36 36" aria-hidden="true">
        <path d="M8 6c2-1 4 0 5 2l2 4c1 2 0 3-1 4l-2 1c1 3 4 6 7 7l1-2c1-1 2-2 4-1l4 2c2 1 3 3 2 5l-1 2c-2 2-5 3-8 2C13 29 7 23 5 15c-1-3 0-6 2-8z" fill="#f07a32"/>
        <path d="M21 8a8 8 0 0 1 7 7M21 3a13 13 0 0 1 12 12M21 13a3 3 0 0 1 2 2" stroke="#454547" stroke-width="1.8" fill="none" stroke-linecap="round"/>
      </svg>
      <div>
        <div class="booking-label">BOOK YOUR APPOINTMENT</div>
        <div class="booking-number">0417 865 209</div>
      </div>
    </div>
  </header>

  <div class="hero" role="img" aria-label="Photo of two people reviewing financial charts on a laptop and paperwork at a desk"></div>
  <div class="hero-banner"></div>
  <h1 class="hero-title">Beacon Ledger &amp;<br>Returns Your<br>Local Tax Accountant</h1>

  <div class="offer">
    <div class="offer-lead">we offer</div>
    <div class="offer-title">Services:</div>
  </div>
  <div class="offer-rule"></div>

  <div class="service" style="left:46px;top:808px">
    <span class="service-icon"><svg viewBox="0 0 28 28"><path d="M7 3h11l4 4v18H7z"/><path d="M10 9h8M10 13h8M10 17h5"/></svg></span>
    Individual &amp; Company Tax Returns
  </div>
  <div class="service" style="left:46px;top:873px">
    <span class="service-icon"><svg viewBox="0 0 28 28"><path d="M14 3l6 2v5c0 4-3 6-6 7-3-1-6-3-6-7V5z"/><path d="M3 19l5-2 6 4 6-4 5 2M8 21l3 3M14 21l3 3"/></svg></span>
    Company &amp; Trust formation
  </div>
  <div class="service" style="left:46px;top:938px">
    <span class="service-icon"><svg viewBox="0 0 28 28"><circle cx="10" cy="7" r="3"/><path d="M5 17c0-4 2-6 5-6s5 2 5 6M4 19h16M7 19v6M17 19v6M18 4h6v6h-6z"/></svg></span>
    Business Advisory
  </div>
  <div class="service" style="left:414px;top:938px">
    <span class="service-icon"><svg viewBox="0 0 28 28"><path d="M10 3h12v22H10z"/><path d="M5 10h9v15H5zM7 13h5M7 17h2M11 17h1M7 21h2M11 21h1M14 8h6M16 13h4M16 17h4"/></svg></span>
    Bookkeeping
  </div>
  <div class="service" style="left:46px;top:1004px">
    <span class="service-icon"><svg viewBox="0 0 28 28"><path d="M9 25v-5c-3-2-5-5-5-9a10 10 0 0 1 20 0l2 5h-3v4h-4v5"/><path d="M11 9c1-2 4-2 5 0M10 13c2 1 5 1 7-1"/></svg></span>
    BAS &amp; IAS
  </div>
  <div class="service" style="left:298px;top:1004px">
    <span class="service-icon"><svg viewBox="0 0 28 28"><path d="M3 6l5-2 6 3M10 10l8-4 6 10-8 4z"/><circle cx="17" cy="13" r="2"/><path d="M5 22h8l8-3 3 2-8 4H5"/></svg></span>
    Payroll
  </div>
  <div class="service" style="left:499px;top:1004px">
    <span class="service-icon"><svg viewBox="0 0 28 28"><path d="M5 3h14v22H5z"/><path d="M8 7l4 4M8 11h0M12 7h0M8 15h8M8 18h6M8 21h4"/><circle cx="20" cy="21" r="4"/><path d="M18.5 19.5l3 3M21.5 19.5l-3 3"/></svg></span>
    TPAR
  </div>

  <div class="contact-band">
    <div class="contact-item" style="left:35px">
      <span class="contact-icon"><svg viewBox="0 0 16 16"><path d="M2 4h12v9H2z"/><path d="M2 4l6 5 6-5"/></svg></span>
      dovpelk@blrau.com.au
    </div>
    <div class="contact-item" style="left:343px">
      <span class="contact-icon"><svg viewBox="0 0 16 16"><path d="M8 15s5-5 5-8.5a5 5 0 0 0-10 0C3 10 8 15 8 15z"/><circle cx="8" cy="6.5" r="1.8"/></svg></span>
      9 Mirra Close, Tarwin Heights
    </div>
  </div>

  <div class="abn">
    <span class="abn-line"></span>
    <span><span class="abn-label">ABN:</span> 71 284 519 036</span>
    <span class="abn-line"></span>
  </div>

</div>
</body>
</html>
```